Business Card Design

We are a commercial real estate brokerage in San Francisco, leasing office buildings downtown.
I would like a clean, elegant look. Simple but powerful .

Industry/Entity Type

Business

Contact Information for Business Card

Colin Farrow
lic# 07281549
415.555.0172
colin@tarvo-commercial.example
tarvo-commercial.example

```html
<!DOCTYPE html>
<html lang="en">
<head>
<meta charset="utf-8">
<title>Tarvo Commercial — Business Card</title>
<link rel="stylesheet" href="https://fonts.googleapis.com/css2?family=Arimo:wght@400;700&display=swap">
<style>
  :root {
    --page-bg: #ffffff;
    --card-bg: #ffffff;
    --card-border: #a9a9a9;
    --brand-slate: #7a89a3;
    --band-dark: #03030f;
    --band-navy: #0a1a3a;
    --band-blue: #0f3a66;
    --band-green: #0d2a22;
    --strip-top: #8aaad6;
    --strip-bottom: #7b96c0;
    --text-light: #ffffff;
  }
  * { box-sizing: border-box; margin: 0; padding: 0; }
  html, body {
    width: 1200px;
    height: 1000px;
    overflow: hidden;
    background: var(--page-bg);
    font-family: "Arimo", Helvetica, Arial, sans-serif;
  }
  .card {
    position: absolute;
    left: 56px;
    top: 31px;
    width: 1087px;
    height: 637px;
    background: var(--card-bg);
    border: 1px solid var(--card-border);
    overflow: hidden;
  }
  .brand {
    position: absolute;
    left: 0; top: 0;
    width: 100%;
    height: 306px;
    display: flex;
    align-items: center;
    justify-content: center;
    gap: 26px;
  }
  .brand-mark {
    width: 34px;
    height: 34px;
    background: var(--brand-slate);
  }
  .brand-name {
    color: var(--brand-slate);
    font-weight: 700;
    font-size: 78px;
    letter-spacing: 2px;
    line-height: 1;
  }
  .contact-band {
    position: absolute;
    left: 0; top: 306px;
    width: 100%;
    height: 239px;
  }
  .contact-backdrop {
    position: absolute;
    inset: 0;
    background:
      radial-gradient(ellipse 380px 200px at 85% 25%, var(--band-blue) 0%, transparent 70%),
      radial-gradient(ellipse 300px 180px at 12% 40%, var(--band-green) 0%, transparent 70%),
      radial-gradient(ellipse 520px 260px at 70% 55%, var(--band-navy) 0%, transparent 75%),
      var(--band-dark);
  }
  .contact {
    position: relative;
    text-align: center;
    color: var(--text-light);
    padding-top: 34px;
  }
  .contact-name {
    font-weight: 700;
    font-size: 39px;
    line-height: 46px;
    margin-bottom: 14px;
  }
  .contact-line {
    font-size: 27px;
    line-height: 33.5px;
  }
  .web-strip {
    position: absolute;
    left: 0; top: 545px;
    width: 100%;
    height: 69px;
    background: linear-gradient(var(--strip-top), var(--strip-bottom));
    color: var(--text-light);
    font-size: 27px;
    display: flex;
    align-items: center;
    justify-content: center;
  }
</style>
</head>
<body>
  <div class="card">
    <header class="brand">
      <span class="brand-mark"></span>
      <span class="brand-name">TARVO COMMERCIAL</span>
    </header>

    <section class="contact-band">
      <div class="contact-backdrop" role="img" aria-label="Abstract dark navy background with soft blue and green curved light streaks"></div>
      <div class="contact">
        <h1 class="contact-name">COLIN FARROW</h1>
        <p class="contact-line">lic# 07281549</p>
        <p class="contact-line">415.555.0172</p>
        <p class="contact-line">colin@tarvo-commercial.example</p>
      </div>
    </section>

    <footer class="web-strip">tarvo-commercial.example</footer>
  </div>
</body>
</html>
```